Microlight Aircraft Website Project

Need a website designed, or at least a template made, that my web programmer can work with here. We are a new manufacturer of microlight aircraft & powered hang gliders. Our company name is Bright Fern. We manufacture portable utility aircraft in the Light Sport category (formerly known as Ultralights or Microlights). Our particular design is a 2-seat powered hang glider and caters to those who want to go explore the backcountry. We are not necessarily aviation nuts, but more into the development of a flying utility vehicle for extreme exploration and expeditions. We have been importing these aircraft from 3 countries for 15 years and have supplied over 200 expedition-quality aircraft world-wide. We are now manufacturing here in the US.

Industry/Entity Type

Manufacturer

Coding

Coded - Design and coding required

```html
<!DOCTYPE html>
<html lang="en">
<head>
<meta charset="utf-8">
<title>Bright Fern – Microlight Aircraft</title>
<link rel="stylesheet" href="https://fonts.googleapis.com/css2?family=Montserrat:wght@600&family=Roboto:wght@400;500&display=swap">
<style>
:root{
  --navy:#323579;
  --navy-deep:#1f2660;
  --blue:#3a5aa8;
  --ink:#162058;
  --grey-bg:#efefef;
  --text:#7a7a7a;
  --text-dark:#555;
  --white:#fff;
}
*{margin:0;padding:0;box-sizing:border-box}
html,body{width:1200px;height:2326px;overflow:hidden}
body{position:relative;background:var(--white);font-family:"Roboto",Arial,sans-serif;color:var(--text)}
.abs{position:absolute}

/* hero */
.hero-photo{left:0;top:0;width:1200px;height:677px;
  background:linear-gradient(180deg,#b9cfe6 0%,#8fa6bd 22%,#6e7f84 38%,#4e6a4a 62%,#2f4a2a 100%)}
.brand{left:78px;top:110px;display:flex;align-items:center;gap:12px;
  font-family:"Montserrat",sans-serif;font-weight:600;font-size:26px;color:var(--ink);letter-spacing:1px}
.brand-mark{width:22px;height:22px;background:var(--ink)}
.hero-panel{left:0;top:321px;width:684px;height:229px;background:rgba(50,53,121,.95);padding:22px 0 0 111px}
.hero-title{font-family:"Montserrat",sans-serif;font-weight:600;font-size:41px;color:var(--white);letter-spacing:.5px}
.hero-text{font-size:19px;line-height:30px;color:var(--white);margin-top:8px;width:480px}
.btn{display:inline-block;background:var(--navy);color:var(--white);font-size:20px;text-align:center;text-transform:uppercase}
.hero-btn{left:108px;top:468px;width:183px;height:62px;line-height:62px;background:var(--navy-deep)}

/* nav */
.nav{left:0;top:677px;width:1200px;height:63px;background:var(--navy)}
.nav a{position:absolute;top:0;height:63px;line-height:63px;color:var(--white);font-size:16px;text-decoration:none}
.nav .active{background:var(--navy-deep);width:111px;text-align:center}
.nav-search{left:1079px;top:696px}

/* sections */
.section-title{font-size:43px;font-weight:400;color:var(--ink);text-align:center}
.section-title span,.feature-title span{color:var(--blue)}
.welcome-title{left:0;top:795px;width:1200px}
.welcome-text{left:225px;top:858px;width:750px;font-size:15px;line-height:25px;text-align:center;color:#999}
.welcome-btn{left:508px;top:1020px;width:184px;height:62px;line-height:62px}

.features{left:0;top:1146px;width:1200px;height:634px;background:var(--grey-bg)}
.photo{border-radius:4px}
.craft-one{left:116px;top:1201px;width:287px;height:202px;background:radial-gradient(ellipse at 50% 45%,#c23a2c 0%,#7d8fc4 45%,rgba(239,239,239,0) 72%)}
.craft-two{left:794px;top:1519px;width:304px;height:132px;background:radial-gradient(ellipse at 50% 45%,#cc3a30 0%,#d98a86 40%,rgba(239,239,239,0) 72%)}
.feature-title{font-size:37px;font-weight:400;color:var(--ink)}
.feature-text{font-size:15px;line-height:25px;color:var(--text-dark)}
.f1-title{left:460px;top:1193px}
.f1-text{left:461px;top:1242px;width:612px}
.f1-btn{left:462px;top:1333px;width:183px;height:62px;line-height:62px}
.divider{left:78px;top:1459px;width:1046px;height:1px;background:#dedede}
.f2-title{left:80px;top:1518px}
.f2-text{left:80px;top:1565px;width:612px}
.f2-btn{left:78px;top:1656px;width:183px;height:62px;line-height:62px}

/* news */
.news-title{left:0;top:1835px;width:1200px}
.news-item{top:1922px;width:340px}
.date{position:absolute;left:0;top:0;width:88px;height:89px;border-radius:4px;overflow:hidden}
.date-day{height:50px;background:var(--grey-bg);color:var(--ink);font-size:33px;font-weight:500;text-align:center;line-height:52px}
.date-month{height:39px;background:var(--navy);color:var(--white);font-size:19px;text-align:center;line-height:39px}
.news-head{position:absolute;left:106px;top:0;width:230px;font-size:17px;line-height:20px;color:var(--ink);font-weight:400}
.news-text{position:absolute;left:106px;top:56px;width:230px;font-size:14px;line-height:26px;color:#999}

/* contact strip */
.contact{left:0;top:2105px;width:1200px;height:158px;background:var(--grey-bg)}
.contact-sep{top:2128px;width:1px;height:112px;background:#cfcfcf}
.contact-icon{top:2160px}
.contact-label{font-size:15px;line-height:26px;color:var(--text-dark)}
.contact-name{color:var(--navy)}

/* footer */
.footer{left:0;top:2263px;width:1200px;height:63px;background:var(--navy);color:#d7d9ee;font-size:15px;line-height:63px}
.footer-copy{position:absolute;left:78px}
.footer a{position:absolute;top:0;color:var(--white);text-decoration:none;font-size:15px}
</style>
</head>
<body>

<header>
  <div class="abs hero-photo" role="img" aria-label="Aerial photograph of a microlight aircraft flying over mountains and a lake"></div>
  <div class="abs brand"><span class="brand-mark"></span>BRIGHT FERN</div>
  <div class="abs hero-panel">
    <h1 class="hero-title">MICROLIGHT AIRCRAFT</h1>
    <p class="hero-text">Lorem Ipsum is simply dummy text of the printing and typesetting industry. Lorem Ipsum has been the..</p>
  </div>
  <a class="abs btn hero-btn">Book Now</a>

  <nav class="abs nav">
    <a class="active" style="left:78px">HOME</a>
    <a style="left:222px">ABOUT</a>
    <a style="left:342px">PRODUCT</a>
    <a style="left:481px">NEWS</a>
    <a style="left:598px">CONTACT</a>
  </nav>
  <svg class="abs nav-search" width="26" height="26" viewBox="0 0 26 26" aria-label="Search">
    <circle cx="11" cy="11" r="8" fill="none" stroke="#fff" stroke-width="3.5"/>
    <line x1="17" y1="17" x2="24" y2="24" stroke="#fff" stroke-width="4" stroke-linecap="round"/>
  </svg>
</header>

<section>
  <h2 class="abs section-title welcome-title"><span>WELCOME TO</span> BRIGHT FERN</h2>
  <p class="abs welcome-text">Lorem Ipsum is simply dummy text of the printing and typesetting industry. Lorem Ipsum has been the industry's standard dummy text ever since the 1500s, when an unknown printer took a galley of type and scrambled it to make a type specimen book. It has survived not only five centuries, but also the leap into electronic typesetting, remaining essentially unchanged. It was popularised in the 1960s with the release of Lettrafold sheets containing Lorem Ipsum passages, and more recently with desktop publishing software like Alder PageCraft including versions of Lorem Ipsum.</p>
  <a class="abs btn welcome-btn">Know More</a>
</section>

<section>
  <div class="abs features"></div>
  <div class="abs photo craft-one" role="img" aria-label="Red and blue two-seat microlight aircraft"></div>
  <h3 class="abs feature-title f1-title"><span>MICROLIGHT</span> AIRCRAFT</h3>
  <p class="abs feature-text f1-text">Lorem Ipsum is simply dummy text of the printing and typesetting industry. Lorem Ipsum has been the industry's standard dummy text ever since the 1500s, when an unknown printer took a galley of type and scrambled it to make a type specimeng...</p>
  <a class="abs btn f1-btn">Know More</a>
  <div class="abs divider"></div>
  <h3 class="abs feature-title f2-title"><span>POWERED</span> HANG GLIDERS</h3>
  <p class="abs feature-text f2-text">Lorem Ipsum is simply dummy text of the printing and typesetting industry. Lorem Ipsum has been the industry's standard dummy text ever since the 1500s, when an unknown printer took a galley of type and scrambled it to make a type specimeng...</p>
  <a class="abs btn f2-btn">Know More</a>
  <div class="abs photo craft-two" role="img" aria-label="Red powered hang glider in flight"></div>
</section>

<section>
  <h2 class="abs section-title news-title"><span>LATEST</span> NEWS</h2>
  <article class="abs news-item" style="left:78px">
    <div class="date"><div class="date-day">21</div><div class="date-month">Feb</div></div>
    <h4 class="news-head">Lorem Ipsum is simply dummy text of</h4>
    <p class="news-text">Lorem Ipsum is simply dummy text of Lorem Ipsum is simply dummy text of ....</p>
  </article>
  <article class="abs news-item" style="left:433px">
    <div class="date"><div class="date-day">20</div><div class="date-month">Feb</div></div>
    <h4 class="news-head" style="top:4px">Lorem Ipsum is simply dummy text of</h4>
    <p class="news-text">Lorem Ipsum is simply dummy text of Lorem Ipsum is simply dummy text of ....</p>
  </article>
  <article class="abs news-item" style="left:788px">
    <div class="date"><div class="date-day">19</div><div class="date-month">Feb</div></div>
    <h4 class="news-head">Lorem Ipsum is simply dummy text of</h4>
    <p class="news-text">Lorem Ipsum is simply dummy text of Lorem Ipsum is simply dummy text of ....</p>
  </article>
</section>

<section>
  <div class="abs contact"></div>
  <svg class="abs contact-icon" style="left:76px" width="52" height="52" viewBox="0 0 52 52" aria-label="Location">
    <circle cx="26" cy="26" r="26" fill="#323579"/>
    <path d="M26 14a8 8 0 0 0-8 8c0 6 8 15 8 15s8-9 8-15a8 8 0 0 0-8-8z" fill="#fff"/>
    <circle cx="26" cy="22" r="3" fill="#323579"/>
  </svg>
  <div class="abs contact-label" style="left:150px;top:2170px"><span class="contact-name">BRIGHT FERN</span><br>Lorem Ipsum is simply dummy text of</div>
  <div class="abs contact-sep" style="left:414px"></div>
  <svg class="abs contact-icon" style="left:428px" width="52" height="52" viewBox="0 0 52 52" aria-label="Email">
    <circle cx="26" cy="26" r="25" fill="none" stroke="#323579" stroke-width="1.5"/>
    <rect x="16" y="19" width="20" height="14" rx="1.5" fill="#323579"/>
    <path d="M16 20l10 7 10-7" fill="none" stroke="#fff" stroke-width="1.6"/>
  </svg>
  <div class="abs contact-label" style="left:507px;top:2173px">info@brightfern.com</div>
  <div class="abs contact-sep" style="left:767px"></div>
  <svg class="abs contact-icon" style="left:780px" width="52" height="52" viewBox="0 0 52 52" aria-label="Phone">
    <circle cx="26" cy="26" r="25" fill="none" stroke="#323579" stroke-width="1.5"/>
    <path d="M19 16l4 0 2 6-3 2c1 3 3 5 6 6l2-3 6 2v4c0 1-1 2-2 2-9 0-17-8-17-17 0-1 1-2 2-2z" fill="#323579"/>
  </svg>
  <div class="abs contact-label" style="left:863px;top:2173px">+(1) 0555 010 200</div>
</section>

<footer class="abs footer">
  <span class="footer-copy">© BRIGHT FERN - 2016, All rights resreved.</span>
  <a style="left:736px">Home</a>
  <a style="left:812px">About</a>
  <a style="left:889px">Product</a>
  <a style="left:984px">News</a>
  <a style="left:1061px">Contact</a>
</footer>

</body>
</html>
```